Teams Background for client video calls - giving them a feel who we are

I'm keen to create a background artwork of a modern dynamic office that also reflects our values which are all about transparency, humility, integrity etc. Our company is called Corvelle Bridging. Our behaviours are agility, excellence and precision. You can find all about our colours and branding under our website www.corvellebridging.com

Target Market(s)

IT Recruitment

Industry/Entity Type

IT Recruitment

Other font styles liked:
• as per our website www.corvellebridging.com

Colors
0054AA
0677BA
7BADD7
CADEEF
E8F1F8

Requirements
Must have
• A modern cool dynamic work office design incooperating our logo and what we stand for in terms of colours and our values and behaviours we live as a company. As i founded the office in the cabin but now we are in a modern office a blend would work i think.

```html
<!DOCTYPE html>
<html lang="en">
<head>
<meta charset="utf-8">
<title>Corvelle Bridging – Call Background</title>
<link rel="stylesheet" href="https://fonts.googleapis.com/css2?family=Teko:wght@600&display=swap">
<style>
  :root {
    --navy-deep: #1b3a78;
    --navy-mid: #264b93;
    --navy-light: #2f58a3;
    --teal: #17a79b;
    --gold: #f6b21c;
    --white: #ffffff;
  }
  html, body {
    margin: 0;
    padding: 0;
    width: 1200px;
    height: 675px;
    overflow: hidden;
  }
  .canvas {
    position: relative;
    width: 1200px;
    height: 675px;
    overflow: hidden;
    font-family: "Teko", "Arial Narrow", sans-serif;
    color: var(--white);
  }
  .office-photo {
    position: absolute;
    inset: 0;
    background: linear-gradient(180deg, var(--navy-mid) 0%, var(--navy-light) 55%, var(--navy-deep) 100%);
  }
  .light-bands {
    position: absolute;
    inset: 0;
  }
  .decor {
    position: absolute;
    inset: 0;
  }
  .brand-name {
    position: absolute;
    left: 60px;
    top: 52px;
    margin: 0;
    font-size: 34px;
    font-weight: 600;
    line-height: 0.95;
    letter-spacing: 0.5px;
    color: var(--white);
  }
  .values {
    position: absolute;
    left: 82px;
    top: 175px;
    margin: 0;
    padding: 0;
    list-style: none;
  }
  .values li {
    font-size: 44px;
    font-weight: 600;
    line-height: 55px;
    height: 55px;
    letter-spacing: 0.3px;
  }
</style>
</head>
<body>
<div class="canvas">
  <div class="office-photo" role="img" aria-label="Photo of a bright modern meeting room with a white table, chairs, steel-framed windows and plants, tinted in deep blue"></div>

  <svg class="light-bands" width="1200" height="675" viewBox="0 0 1200 675" aria-hidden="true">
    <polygon points="470,0 700,0 290,675 80,675" fill="#ffffff" opacity="0.05"/>
    <polygon points="690,0 780,0 530,675 290,675" fill="#ffffff" opacity="0.04"/>
  </svg>

  <svg class="decor" width="1200" height="675" viewBox="0 0 1200 675" aria-hidden="true">
    <defs>
      <mask id="outside-big-ring">
        <rect width="1200" height="675" fill="#fff"/>
        <circle cx="1163" cy="638" r="114" fill="#000"/>
      </mask>
    </defs>
    <line class="top-rule" x1="708" y1="67.5" x2="1200" y2="67.5" stroke="var(--teal)" stroke-width="3.5"/>
    <line class="value-rail" x1="62" y1="157" x2="62" y2="675" stroke="var(--gold)" stroke-width="2.6"/>
    <g class="value-nodes" fill="none" stroke="var(--gold)" stroke-width="3">
      <circle cx="62" cy="197" r="12.5"/>
      <circle cx="62" cy="250.5" r="12.5"/>
      <circle cx="62" cy="306" r="12.5"/>
    </g>
    <g class="corner-rings" fill="none" stroke="var(--teal)" stroke-width="3">
      <circle cx="1163" cy="638" r="114"/>
      <circle cx="1207" cy="531" r="77" mask="url(#outside-big-ring)"/>
      <circle cx="1006" cy="764" r="133" mask="url(#outside-big-ring)"/>
    </g>
  </svg>

  <p class="brand-name">Corvelle<br>Bridging</p>

  <ul class="values">
    <li>AGILE</li>
    <li>EXCELLENCE</li>
    <li>PRECISION</li>
  </ul>
</div>
</body>
</html>
```